Word Press Website design

Harborlight Studio is a Website design, SEO, Social Networking and app development company. We would like to see what you can do to create a new, relevant and exciting design for us. This is our first project for Pixel Meadow so we thought we would test drive this site.  We would like to leave it up to your creative interpretation of the new design, but you can checkout our old design at www.harborlightstudiohub.example
We are always looking for new talent for future projects. Wow us with your designs and there will be future work for you.

Target Market(s)
Our target customers are medium sized businesses of all vertical markets.
Industry/Entity Type
Internet
Font styles to use
Requirements
Must have
- Easy to navigate, HTML 5 sliders, modern
Nice to have
- Bring your graphic talents with an outside of the box design that will standout to prospective clients.

```html
<!DOCTYPE html>
<html lang="en">
<head>
<meta charset="utf-8">
<title>Harborlight Studio – Kansas City Website Design</title>
<link href="https://fonts.googleapis.com/css2?family=Open+Sans:ital,wght@0,400;0,600;0,700;1,400;1,600;1,700&display=swap" rel="stylesheet">
<style>
  :root {
    --white: #ffffff;
    --ink: #2a2a2a;
    --muted: #9a9a9a;
    --rule: #ececec;
    --accent: #e8562a;
    --band-light: #d9a25e;
    --band-dark: #b9783a;
    --band-text: #3a2a1a;
    --button: #1e1e1e;
    --hero-cool: #c9cfd6;
    --hero-mid: #b98a5a;
    --hero-warm: #8a4a1c;
    --hero-deep: #5a2e12;
  }
  * { margin: 0; padding: 0; box-sizing: border-box; }
  html, body { width: 1200px; height: 675px; overflow: hidden; background: var(--white); }
  body { font-family: "Open Sans", Arial, sans-serif; color: var(--ink); position: relative; }

  .top-bar {
    height: 28px; display: flex; align-items: center; justify-content: space-between;
    padding: 0 240px 0 250px; border-bottom: 1px solid var(--rule);
    font-size: 9px; color: var(--muted);
  }
  .social-list { display: flex; gap: 8px; }
  .social-dot { width: 8px; height: 8px; border-radius: 50%; background: #c4c4c4; }
  .contact-list { display: flex; gap: 36px; }
  .contact-item { display: flex; align-items: center; gap: 6px; }

  .site-header {
    height: 78px; display: flex; align-items: center; justify-content: space-between;
    padding: 0 230px 0 240px;
  }
  .brand { display: flex; align-items: center; gap: 10px; }
  .brand-square { width: 30px; height: 30px; background: var(--ink); }
  .brand-name { font-weight: 700; font-size: 15px; line-height: 1.05; color: var(--ink); }
  .main-nav { display: flex; align-items: center; gap: 26px; font-size: 10px; font-weight: 700; text-transform: uppercase; }
  .main-nav a { color: var(--ink); text-decoration: none; }
  .main-nav a.is-current { color: var(--accent); }

  .hero {
    position: relative; height: 360px;
  }
  .hero-photo {
    position: absolute; inset: 0;
    background: linear-gradient(100deg, var(--hero-cool) 0%, #b9a894 22%, var(--hero-mid) 45%, var(--hero-warm) 75%, var(--hero-deep) 100%);
  }
  .hero-copy {
    position: absolute; left: 505px; top: 108px; width: 430px; color: var(--white);
    text-shadow: 0 1px 2px rgba(0,0,0,.35);
  }
  .hero-title { font-size: 15px; font-weight: 700; text-transform: uppercase; margin-bottom: 16px; letter-spacing: .2px; }
  .hero-copy p { font-size: 15px; font-style: italic; line-height: 1.3; margin-bottom: 14px; }
  .hero-copy strong { font-weight: 700; }

  .quote-band {
    height: 80px; display: flex; align-items: center; justify-content: space-between;
    padding: 0 260px 0 170px;
    background: linear-gradient(90deg, var(--band-dark), var(--band-light) 50%, var(--band-dark));
  }
  .quote-text { font-size: 17px; font-weight: 700; font-style: italic; text-transform: uppercase; color: var(--band-text); }
  .quote-button {
    background: var(--button); color: var(--white); font-size: 15px; font-weight: 700;
    text-transform: uppercase; padding: 12px 26px; border-radius: 3px; text-decoration: none;
  }

  .feature-row { display: flex; gap: 32px; padding: 24px 0 0 150px; }
  .feature-photo { width: 222px; height: 110px; }
  .feature-photo.is-desk { background: linear-gradient(120deg, #cfc7bd, #8d7c6c); }
  .feature-photo.is-workspace { background: linear-gradient(120deg, #dedbd5, #a7a39b); }
  .feature-photo.is-office { background: linear-gradient(120deg, #e9e6e0, #b6a08a); }
</style>
</head>
<body>
  <div class="top-bar">
    <div class="social-list">
      <span class="social-dot"></span><span class="social-dot"></span><span class="social-dot"></span><span class="social-dot"></span>
    </div>
    <div class="contact-list">
      <span class="contact-item">Mon - Fri 8:00 - 17:00</span>
      <span class="contact-item">+1 555 014 2290</span>
      <span class="contact-item">hello@harborlight.example</span>
    </div>
  </div>

  <header class="site-header">
    <div class="brand">
      <span class="brand-square"></span>
      <span class="brand-name">Harborlight<br>Studio</span>
    </div>
    <nav class="main-nav">
      <a href="#" class="is-current">Home</a>
      <a href="#">Products</a>
      <a href="#">What we do</a>
      <a href="#">About us</a>
      <a href="#">Blog</a>
      <a href="#">Contact us</a>
      <svg width="12" height="12" viewBox="0 0 12 12" aria-label="Search"><circle cx="5" cy="5" r="3.6" fill="none" stroke="#2a2a2a" stroke-width="1.6"/><line x1="7.6" y1="7.6" x2="11" y2="11" stroke="#2a2a2a" stroke-width="1.6"/></svg>
    </nav>
  </header>

  <section class="hero">
    <div class="hero-photo" role="img" aria-label="Close-up photo of eyeglasses resting on a laptop keyboard in warm light"></div>
    <div class="hero-copy">
      <h1 class="hero-title">Kansas City Website Design - Harborlight Studio, L.L.C.</h1>
      <p>Do you want us to tell you the truth about <strong>Harborlight Studio</strong>, or tell you what you want to hear?</p>
      <p>Just the facts then: Harborlight Studio invented the Internet...it is even named after us! Ok...truth is, <strong>Harborlight Studio</strong> has a long history of building high performance Websites.</p>
    </div>
  </section>

  <section class="quote-band">
    <span class="quote-text">Get in touch today for a free quote</span>
    <a href="#" class="quote-button">Contact us</a>
  </section>

  <section class="feature-row">
    <div class="feature-photo is-desk" role="img" aria-label="Photo of hands working at a laptop"></div>
    <div class="feature-photo is-workspace" role="img" aria-label="Photo of a tidy desk with phone, glasses and plant"></div>
    <div class="feature-photo is-office" role="img" aria-label="Photo of a bright office workspace"></div>
  </section>
</body>
</html>
```